Dental Practice Billboard Design

We are a newer dental practice in need of a simple but appealing billboard for our growing dental practice to attract new patients. The practice is owned by husband and wife dentists and is family friendly in a small town in Kentucky. We try to be very friendly and caring to our patients. Would prefer a blue background for the billboard and our tooth logo to be prominent. We are partial to the Patua One font used in the image below but please feel free to tweak it as you deem necessary. The shape of the uppercase D and lowercase g are why we like that font, so fonts with a similarly shaped “D” and “g” would work as well. Please include our phone number (606) 847-3962. Please see our website Harlowfamilydentistry.com for more info on the practice if needed. Thank you! Looking forward to seeing your creation.
Updates

The dimensions will be 12ft x 24ft (3.6576m x 7.3152m). Apologies for not including this in the original prompt. Thank you all for your submissions.

Industry/Entity Type

Dental

Font styles to use
Other font styles liked:
• Patua One

Colors
0054AA
0677BA
7BADD7
CADEEF
E8F1F8
0094D4
00A9DD
6FCCEA
C7EBF8
E9F6FB
00AB8E
00BBA5
67D7C9
C6EFE9
E9F9F6
59FF00
82FF00
B8FF75
E3FFCB
F4FFEA

Requirements
Must have
• Phone number, website, Logo, Practice name “Harlow Family Dentistry”
Should not have
• A tagline or slogan

```html
<!DOCTYPE html>
<html lang="en">
<head>
<meta charset="utf-8">
<title>Harlow Family Dentistry – Billboard</title>
<link href="https://fonts.googleapis.com/css2?family=Patua+One&display=swap" rel="stylesheet">
<style>
  :root {
    --page-bg: #e9edf2;
    --brand-blue: #0054aa;
    --accent-green: #1fae3e;
    --white: #ffffff;
    --skin-light: #ecc9b0;
    --skin-mid: #d6a487;
    --skin-deep: #b98168;
  }
  * { margin: 0; padding: 0; box-sizing: border-box; }
  html, body {
    width: 990px; height: 1200px; overflow: hidden;
    background: var(--page-bg);
    font-family: "Patua One", Georgia, serif;
    font-weight: 400;
  }
  .billboard {
    position: absolute; left: 45px; top: 413px;
    width: 900px; height: 374px;
    background: var(--brand-blue);
    overflow: hidden;
    box-shadow: 0 18px 30px rgba(0,0,0,0.18);
  }
  .portrait-photo { position: absolute; inset: 0; width: 900px; height: 374px; }
  .brand { position: absolute; left: 38px; top: 40px; display: flex; align-items: center; gap: 12px; color: var(--white); }
  .brand-mark { width: 62px; height: 62px; border-radius: 50%; background: var(--white); flex: none; }
  .brand-name { font-size: 38px; line-height: 1; font-weight: 400; }
  .brand-sub { font-size: 18px; line-height: 1.2; margin-top: 4px; font-weight: 400; }
  .website-frame {
    position: absolute; left: 26px; top: 150px; width: 507px; height: 100px;
    border: 2px solid var(--accent-green);
  }
  .website {
    position: absolute; left: 26px; top: 150px; width: 507px; height: 100px;
    display: flex; align-items: center; justify-content: center;
    color: var(--white); font-size: 36px; line-height: 1; font-weight: 400;
  }
  .phone {
    position: absolute; left: 218px; top: 298px; width: 310px; height: 41px;
    background: var(--accent-green); border-radius: 21px;
    display: flex; align-items: center;
  }
  .phone-icon {
    width: 46px; height: 46px; margin-left: -2px; border-radius: 50%;
    background: var(--accent-green); border: 3px solid var(--brand-blue);
    display: flex; align-items: center; justify-content: center; flex: none;
  }
  .phone-number { color: var(--white); font-size: 33px; line-height: 1; margin-left: 14px; font-weight: 400; white-space: nowrap; }
</style>
</head>
<body>
  <main class="billboard">
    <svg class="portrait-photo" viewBox="0 0 900 374" role="img" aria-label="Photo of a smiling woman touching her cheek, showing white teeth">
      <defs>
        <linearGradient id="skinTone" x1="0" y1="0" x2="1" y2="1">
          <stop offset="0" stop-color="#ecc9b0"/>
          <stop offset="0.6" stop-color="#d6a487"/>
          <stop offset="1" stop-color="#b98168"/>
        </linearGradient>
      </defs>
      <path d="M497 0 C520 40 545 120 575 190 C600 250 640 300 705 326 L643 374 L900 374 L900 0 Z" fill="url(#skinTone)"/>
    </svg>

    <div class="brand">
      <span class="brand-mark"></span>
      <div class="brand-text">
        <div class="brand-name">Harlow</div>
        <div class="brand-sub">Family Dentistry</div>
      </div>
    </div>

    <div class="website-frame"></div>
    <p class="website">Harlowfamilydentistry.com</p>

    <div class="phone">
      <span class="phone-icon">
        <svg width="24" height="24" viewBox="0 0 24 24" aria-hidden="true">
          <path fill="#fff" d="M6.6 10.8a15.1 15.1 0 0 0 6.6 6.6l2.2-2.2a1 1 0 0 1 1-.25 11.4 11.4 0 0 0 3.6.57 1 1 0 0 1 1 1V20a1 1 0 0 1-1 1A17 17 0 0 1 3 4a1 1 0 0 1 1-1h3.5a1 1 0 0 1 1 1c0 1.25.2 2.45.57 3.6a1 1 0 0 1-.25 1z"/>
        </svg>
      </span>
      <span class="phone-number">(606) 847-3962</span>
    </div>
  </main>
</body>
</html>
```